Simple, Professional and neat business card design for Vellamor Inc.

We're looking to re-vamp our business card design. We're a supplier of innovative feed ingredients for the North American animal agriculture industry. We are located in Lucknow, Ontario, Canada and our flagship product is a product that prevents milk fever in dairy cows when the calve, it is fed before calving and is very effective compared to other alternatives available on the market today.

Our company has Danish roots and we import all of our product from our Danish partner/manufacturer in Denmark. We like our design to embrace high professionalism while remaining neat and simple.

Target Market(s)

B2B, Feed Mills, Veterinary Clinics, Large integrators/producers,

Industry/Entity Type

Agribusiness

Contact Information for Business Card

We like the rounded corners because they make the card easy to sit in a wallet and not many use it so it makes the card stand out, just possibly something to take account for during the design.

As you can also see on the sliders below, looking for a that simple but proffesional scandinavian design.

Requirements
Nice to have
• Rounded corners
Should not have
• Too vibrant

```html
<!DOCTYPE html>
<html lang="en">
<head>
<meta charset="utf-8">
<title>Vellamor Inc. – Business Card</title>
<link rel="stylesheet" href="https://fonts.googleapis.com/css2?family=Open+Sans:wght@400;600;800&family=Roboto:wght@400;500&display=swap">
<style>
  :root {
    --backdrop: #3b3b3d;
    --card-black: #1e1e21;
    --emboss: #5d5d62;
    --tagline: #8a8a8f;
    --paper: #ffffff;
    --brand-blue: #1a3f8f;
    --ink: #2b2b2b;
    --sand: #d8c39a;
    --faint: #eeeeef;
  }
  * { margin: 0; padding: 0; box-sizing: border-box; }
  html, body { width: 799px; height: 1200px; overflow: hidden; }
  body {
    background: var(--backdrop);
    font-family: "Roboto", sans-serif;
    position: relative;
  }
  .card {
    position: absolute;
    left: 80px;
    width: 640px;
    height: 366px;
    border-radius: 26px;
    overflow: hidden;
  }

  /* Front */
  .card-front { top: 150px; background: var(--card-black); }
  .front-mark {
    position: absolute;
    top: 110px; left: 0; right: 0;
    display: flex; align-items: center; justify-content: center; gap: 14px;
  }
  .front-mark .dot {
    width: 30px; height: 30px; border-radius: 50%;
    background: var(--emboss);
  }
  .front-mark .wordmark {
    font-family: "Open Sans", sans-serif;
    font-weight: 800;
    font-size: 38px;
    color: var(--emboss);
    letter-spacing: 1px;
    text-transform: uppercase;
  }
  .tagline {
    position: absolute;
    bottom: 92px; left: 0; right: 0;
    text-align: center;
    font-size: 20px;
    letter-spacing: 1px;
    color: var(--tagline);
    text-transform: uppercase;
  }

  /* Back */
  .card-back { top: 690px; background: var(--paper); }
  .faint-circle {
    position: absolute;
    right: -60px; top: 60px;
    width: 330px; height: 330px; border-radius: 50%;
    background: var(--faint);
  }
  .brand {
    position: absolute; top: 36px; left: 28px;
    display: flex; align-items: center; gap: 18px;
  }
  .brand .square {
    width: 58px; height: 58px; border-radius: 8px;
    background: var(--brand-blue);
  }
  .brand .wordmark {
    font-family: "Open Sans", sans-serif;
    font-weight: 800;
    font-size: 44px;
    color: var(--brand-blue);
    text-transform: uppercase;
    letter-spacing: 0.5px;
  }
  .person { position: absolute; top: 128px; left: 32px; }
  .person .name {
    font-family: "Open Sans", sans-serif;
    font-weight: 800; font-size: 23px; color: var(--brand-blue);
  }
  .person .role { font-size: 14px; color: var(--ink); margin-top: 2px; }
  .person .address { font-size: 15px; color: var(--ink); margin-top: 22px; line-height: 1.4; }

  .contacts {
    position: absolute; top: 182px; left: 372px;
    list-style: none; font-size: 16px; color: var(--ink);
  }
  .contacts li { display: flex; align-items: center; gap: 12px; height: 21px; }
  .contacts svg { width: 13px; height: 13px; fill: var(--brand-blue); flex: none; }

  .sand-band {
    position: absolute; left: 0; bottom: 0;
    width: 300px; height: 16px; background: var(--sand);
  }
  .blue-band {
    position: absolute; right: 0; bottom: 0;
    width: 370px; height: 80px;
    background: var(--brand-blue);
    border-top-left-radius: 34px;
  }
  .social {
    position: absolute; left: 122px; top: 26px;
    display: flex; gap: 8px;
  }
  .social span {
    width: 22px; height: 22px; border-radius: 50%; background: var(--paper);
  }
</style>
</head>
<body>

<section class="card card-front">
  <div class="front-mark">
    <span class="dot"></span>
    <span class="wordmark">Vellamor Inc.</span>
  </div>
  <p class="tagline">Protecting the health of your animals</p>
</section>

<section class="card card-back">
  <div class="faint-circle"></div>

  <div class="brand">
    <span class="square"></span>
    <span class="wordmark">Vellamor Inc.</span>
  </div>

  <div class="person">
    <p class="name">Mikkel Strandgaard</p>
    <p class="role">Managing Director</p>
    <p class="address">BOX 412 Lucknow,<br>Ontario Canada N0G 1A0</p>
  </div>

  <ul class="contacts">
    <li><svg viewBox="0 0 16 16"><rect x="4" y="1" width="8" height="14" rx="2"/></svg>519-555-0148</li>
    <li><svg viewBox="0 0 16 16"><rect x="2" y="5" width="12" height="9" rx="1"/><rect x="4" y="1" width="8" height="4"/></svg>519-555-0172</li>
    <li><svg viewBox="0 0 16 16"><path d="M3 1l3 3-2 2c1 2 3 4 5 5l2-2 3 3-2 3C7 14 2 9 1 3z"/></svg>888-555-0193</li>
    <li><svg viewBox="0 0 16 16"><path d="M1 3h14v10H1z M1 3l7 6 7-6" stroke="#fff" stroke-width="1"/></svg>mikkel@vellamor.com</li>
    <li><svg viewBox="0 0 16 16"><circle cx="8" cy="8" r="7"/><path d="M1 8h14M8 1v14" stroke="#fff" stroke-width="1"/></svg>www.vellamor.com</li>
  </ul>

  <div class="sand-band"></div>
  <div class="blue-band">
    <div class="social"><span></span><span></span></div>
  </div>
</section>

</body>
</html>
```